Poster Design Project- kids dancing/sport

I need a poster design for a childrens dance and sport program!!
I have attached a brochure and logo designs. From the brochure please include information from sections titled "twirl'n'hop" and "themes". Also please put on the phone number and email address (found on the brochure). Emphasis on FUN!! Make poster colourful, very kid friendly and eye catching.
Some other things i would like on the poster are:
"Does your child love to dance, sing and play sport?? Why not enrol them in our fun-filled program?"
"From only $10.00 per class"
"Sign up for your FREE trial class today"
"A fun introduction to the joy of Dance, Sport and Music for 2-6yr olds. Held in your childcare centre!!"
Hi!!
I would like to stress its TRIAL class not TRAIL class. Please feel free to play around with the information, it doesnt need to be in one blurb. Also i have updated the brief. I would like "Does you child love to dance, sing or play sport? Why not enrol in our fun filled program?" or something to that effect!!
Thanks!!!!
2-6yr olds and their parents
Childcare

```html
<!DOCTYPE html>
<html lang="en">
<head>
<meta charset="utf-8">
<title>Twirl'n'Hop – Dance, Sing and Play Sports</title>
<link rel="stylesheet" href="https://fonts.googleapis.com/css2?family=Short+Stack&family=Questrial&family=Mulish:wght@800&family=Arimo:wght@400;700&display=swap">
<style>
  :root{
    --page:#ffffff;
    --red:#dc3545;
    --purple:#5b3fa0;
    --purple-soft:#8a72c4;
    --cream:#fff8d6;
    --lime:#e9e57e;
    --sun:#fde489;
    --green:#a5d17c;
    --ink:#111111;
    --white:#ffffff;
    --skin:#e9c3a6;
  }
  *{margin:0;padding:0;box-sizing:border-box}
  html,body{width:1200px;height:1000px;overflow:hidden;background:var(--page)}
  .canvas{position:relative;width:1200px;height:1000px}
  .poster-art{position:absolute;left:0;top:0}
  .hand{font-family:"Short Stack",cursive}
  .gothic{font-family:"Questrial",sans-serif}
  .list{font-family:"Mulish",sans-serif;font-weight:800}
  .arial{font-family:"Arimo",sans-serif}
  .about{
    position:absolute;left:350px;top:532px;width:250px;
    transform:rotate(-8deg);transform-origin:left top;
    font-family:"Questrial",sans-serif;font-size:9px;line-height:11px;
    color:var(--ink);text-align:justify;
  }
  .about p+p{margin-top:11px}
</style>
</head>
<body>
<div class="canvas">
<svg class="poster-art" width="1200" height="1000" viewBox="0 0 1200 1000">
  <defs>
    <linearGradient id="kidsPhoto" x1="0" y1="0" x2="1" y2="1">
      <stop offset="0" stop-color="var(--purple-soft)"/>
      <stop offset="1" stop-color="var(--purple)"/>
    </linearGradient>
    <radialGradient id="dancerPhoto" cx="0.5" cy="0.5" r="0.6">
      <stop offset="0" stop-color="var(--skin)"/>
      <stop offset="1" stop-color="#c9d4e0"/>
    </radialGradient>
  </defs>

  <!-- poster sheet -->
  <rect class="sheet" x="302" y="56" width="630" height="889" fill="var(--page)"/>

  <!-- top red band -->
  <polygon class="top-band" points="302,56 932,56 932,118 302,132" fill="var(--red)"/>
  <text class="arial" x="348" y="116" font-size="21" font-weight="700" fill="var(--white)">DOES YOUR CHILD LOVE TO</text>

  <!-- children photo panel -->
  <polygon role="img" aria-label="Photo of smiling young children" class="kids-photo"
           points="348,142 932,124 932,340 385,397" fill="url(#kidsPhoto)"/>

  <!-- brand name -->
  <rect x="724" y="82" width="14" height="14" fill="var(--white)"/>
  <text class="list" x="746" y="96" font-size="19" fill="var(--white)">TWIRL'N'HOP</text>

  <!-- headline -->
  <g class="headline hand" fill="var(--cream)" stroke="#3a2a6a" stroke-width="1">
    <text x="420" y="195" font-size="44" transform="rotate(-6 420 195)">Dance, Sing</text>
    <text x="520" y="238" font-size="36" transform="rotate(-6 520 238)">and</text>
    <text x="400" y="298" font-size="46" transform="rotate(-6 400 298)">Play Sports??</text>
  </g>
  <g class="arial" fill="var(--white)" font-size="22" transform="rotate(-7 460 340)">
    <text x="460" y="340">WHY NOT ENROL THEM IN OUR</text>
    <text x="500" y="366">FUN-FILLED PROGRAM?"</text>
  </g>

  <!-- colour fields -->
  <polygon class="theme-field" points="700,344 932,330 932,528 840,740 690,748 640,485" fill="var(--lime)"/>
  <polygon class="about-field" points="302,566 622,500 690,748 706,945 302,945" fill="var(--green)"/>
  <circle class="price-disc" cx="835" cy="855" r="150" fill="var(--sun)"/>
  <rect x="932" y="56" width="268" height="944" fill="var(--page)"/>
  <rect x="302" y="945" width="898" height="55" fill="var(--page)"/>

  <!-- intro -->
  <g transform="rotate(-7 350 440)">
    <text class="gothic" x="350" y="440" font-size="18" fill="var(--ink)">A fun introduction to the joy of</text>
    <text class="hand" x="360" y="465" font-size="23" fill="var(--ink)">Dance, Sport and Music</text>
    <text class="list" x="398" y="488" font-size="20" fill="var(--ink)">FOR 2-6YR OLDS</text>
  </g>

  <!-- dancer photos -->
  <circle cx="880" cy="682" r="56" fill="#eeeeee"/>
  <circle role="img" aria-label="Photo of a boy breakdancing" cx="880" cy="682" r="52" fill="url(#dancerPhoto)"/>
  <circle cx="652" cy="880" r="52" fill="#eeeeee"/>
  <circle role="img" aria-label="Photo of a girl dancing" cx="652" cy="880" r="48" fill="url(#dancerPhoto)"/>

  <!-- theme list -->
  <g class="list" font-size="12.5" fill="var(--ink)" text-anchor="middle">
    <text x="767" y="389">JUMPING JELLYBEANS</text>
    <text x="767" y="405">UNDER THE SEA</text>
    <text x="767" y="421">SUPERHEROS</text>
    <text x="767" y="437">JUNGLE JAM</text>
    <text x="767" y="453">STORYBOOK</text>
    <text x="767" y="469">BALANCING BUGS</text>
    <text x="769" y="485">GYMNASTICS &amp; RHYTHMIC GYMNASTICS</text>
    <text x="767" y="501">DISCO DIVAS</text>
    <text x="767" y="517">HAWAIIAN HOLIDAY</text>
    <text x="767" y="533">CIRCUS</text>
    <text x="767" y="549">SPACE</text>
    <text x="767" y="565">BOWLING AND BALL SKILLS</text>
    <text x="767" y="581">COLOURS AND SHAPES</text>
    <text x="767" y="597">MONSTERS</text>
    <text x="767" y="613">MAGICAL FAIRYTALES</text>
    <text x="767" y="629">SPORT AND CHEERLEADING</text>
    <text x="767" y="645">MEXICAN FIESTA</text>
    <text x="767" y="661">ANIMALS</text>
    <text x="767" y="677">ABORIGINAL ADVENTURE</text>
    <text x="767" y="693">ITS PARTY TIME</text>
  </g>

  <!-- free trial -->
  <ellipse cx="510" cy="805" rx="112" ry="50" fill="var(--red)" transform="rotate(-5 510 805)"/>
  <g fill="var(--white)" text-anchor="middle">
    <text class="gothic" x="510" y="786" font-size="19">SIGN UP for your</text>
    <text class="arial" x="510" y="814" font-size="26" font-weight="700">FREE</text>
    <text class="gothic" x="510" y="838" font-size="17">trial class <tspan class="arial" font-weight="700">TODAY!</tspan></text>
  </g>

  <!-- contact -->
  <text class="gothic" x="345" y="895" font-size="23" fill="var(--ink)">Phone: 0400 555 218</text>
  <text class="gothic" x="333" y="916" font-size="14.5" fill="var(--ink)">Email: twirlnhop@kidmail.com</text>

  <!-- price -->
  <g text-anchor="middle" fill="var(--ink)">
    <text class="gothic" x="815" y="788" font-size="21">FROM ONLY</text>
    <text class="arial" x="815" y="830" font-size="42" font-weight="700">$10.00</text>
    <text class="gothic" x="815" y="862" font-size="30">per class</text>
    <g class="hand" font-size="16" transform="rotate(-4 815 890)">
      <text x="815" y="885">Held in your</text>
      <text x="815" y="905">childcare centre!!</text>
    </g>
  </g>
</svg>

<div class="about">
  <p>Twirl'n'Hop offers little boys and girls a range of FUN classes, held in your childcare centre, that will introduce them to the wonderful world of music, movement and P.E. Every class is a magical place to be with funky music, props, puppets, costumes and exciting equipment! Children will develop a range of skills including balance, co-ordination, confidence, motor skills, creativity, rhythm and much more!!</p>
  <p>Each fortnight there is a different theme where children can express themselves and explore many dance genres as well as yoga, gymnastics, sport, musical instruments and ball skills. Detailed information on each class will be emailed to you every fortnight so you'll always be kept up-to-date with what your child is learning!!</p>
  <p>Twirl'n'Hop also offers birthday parties!!! You can select any of the themes listed, or we can custom make a party to the interest of your child. Your host will come dressed as a character of your choice and keep the children entertained for 1-2hrs. Email us for more information!!</p>
</div>
</div>
</body>
</html>
```